Wine Label for a White and a Red Wine from Italy

We have a very good idea of what we want with artwork. We need you to please design a 'template' with the text so we can change out the artwork from year to year. Samples are shown of what we are looking for. We are looking for options with the two basic designs. Brand name of wine is: Valora di Castegno. Both wines are in a light green Bordeaux-style bottle (note: we don't show a light green bottle in the mockup but please remember the bottle is light green). Artwork is provided. We'd like to see either the green or blue butterfly on the white wine, the red butterfly is for the red wine. Please base the design on the attached label from Brailey and/or the attached label from Chateau Mervanges.

Target Market(s)

Millennials, women

Requirements
Must have
• The artwork (butterflies) attached.
Nice to have
• Elegant, readable fonts. Please make the text so it can be changed by the printer. Please make it so the artwork can be changed too.

```html
<!DOCTYPE html>
<html lang="en">
<head>
<meta charset="utf-8">
<title>Valora di Castegno – Rosso Label Options</title>
<link rel="stylesheet" href="https://fonts.googleapis.com/css2?family=Source+Serif+4:wght@300;400&family=Roboto+Condensed:wght@300&display=swap">
<style>
  :root {
    --backdrop: #b9b9b9;
    --label-paper: #ffffff;
    --ink-brand: #4a4a4a;
    --ink-text: #2f2f2f;
    --ink-soft: #555555;
    --ochre-light: #f1c75a;
    --ochre: #e2a928;
    --ochre-deep: #c98d14;
  }
  * { margin: 0; padding: 0; box-sizing: border-box; }
  html, body {
    width: 1200px;
    height: 1009px;
    overflow: hidden;
  }
  body {
    background: var(--backdrop);
    font-family: "Source Serif 4", Georgia, serif;
    color: var(--ink-text);
  }
  .label-set {
    position: absolute;
    top: 154px;
    left: 122px;
    display: flex;
    gap: 100px;
  }
  .label {
    position: relative;
    width: 428px;
    height: 700px;
    background: var(--label-paper);
    text-align: center;
  }
  .label > * {
    position: absolute;
    left: 0;
    right: 0;
    line-height: 1;
  }
  .brand-name {
    top: 62px;
    font-size: 57px;
    font-weight: 300;
    color: var(--ink-brand);
    letter-spacing: 0.5px;
  }
  .brand-sub {
    top: 116px;
    font-size: 22px;
    font-weight: 300;
    color: var(--ink-soft);
  }
  .artwork { left: auto; right: auto; }
  .artwork--brush {
    top: 150px;
    left: 30px;
    width: 350px;
    height: 300px;
    border-radius: 44% 56% 38% 62% / 40% 34% 66% 60%;
    background: radial-gradient(ellipse at 55% 45%, var(--ochre-light) 0%, var(--ochre) 60%, var(--ochre-deep) 100%);
    transform: rotate(-14deg);
  }
  .artwork--disc {
    top: 166px;
    left: 92px;
    width: 244px;
    height: 244px;
    border-radius: 50%;
    background: radial-gradient(circle at 50% 45%, var(--ochre-light) 0%, var(--ochre) 70%, var(--ochre-deep) 100%);
  }
  .cuvee {
    top: 452px;
    font-family: "Roboto Condensed", "Arial Narrow", sans-serif;
    font-weight: 300;
    font-size: 19px;
    letter-spacing: 0.6px;
    color: var(--ink-text);
  }
  .vintage {
    top: 502px;
    font-size: 18px;
  }
  .wine-type {
    top: 533px;
    font-size: 28px;
  }
  .origin {
    top: 562px;
    font-size: 20px;
    font-weight: 300;
  }
  .producer {
    top: 604px;
    font-size: 15px;
    font-weight: 300;
  }
  .farming {
    top: 639px;
    font-size: 15px;
    font-weight: 300;
  }
</style>
</head>
<body>
  <main class="label-set">
    <article class="label label--brush">
      <h1 class="brand-name">Valora</h1>
      <p class="brand-sub">di Castegno</p>
      <div class="artwork artwork--brush" role="img" aria-label="Blue-green painted butterfly over a loose ochre-yellow brushstroke"></div>
      <p class="cuvee">BARREL SELECT</p>
      <p class="vintage">2018</p>
      <p class="wine-type">Rosso</p>
      <p class="origin">Piemonte, Italy</p>
      <p class="producer">Artisanlly Crafted by Cantina Quattro Colli</p>
      <p class="farming">sustainably farmed</p>
    </article>

    <article class="label label--disc">
      <h1 class="brand-name">Valora</h1>
      <p class="brand-sub">di Castegno</p>
      <div class="artwork artwork--disc" role="img" aria-label="Blue-green painted butterfly on a round ochre-yellow painted disc"></div>
      <p class="cuvee">BARREL SELECT</p>
      <p class="vintage">2018</p>
      <p class="wine-type">Rosso</p>
      <p class="origin">Piemonte, Italy</p>
      <p class="producer">Artisanlly Crafted by Cantina Quattro Colli</p>
      <p class="farming">sustainably farmed</p>
    </article>
  </main>
</body>
</html>
```